Business Card Project

Hello,

Please find attached files for use for our business card design.

We have attached all the version of the trade licensing council to the project for insertion onto our business card.

Details to be on the card are:
We are a construction management company. Please ensure that there is space to add our personal contact details. We would like the cards to be double sided with our logo on one side and our details on the other

Thanks,

Marcus

Good Evening,

Please ensure with all design submissions, that the 'certified works overseer' logo is on the card designs.

Thanks,

Marcus

Industry/Entity Type

Construction

```html
<!DOCTYPE html>
<html lang="en">
<head>
<meta charset="utf-8">
<title>Keelvale Group – Business Card</title>
<link rel="stylesheet" href="https://fonts.googleapis.com/css2?family=Arimo:wght@400;700&display=swap">
<style>
  :root {
    --bg: #e9e6e2;
    --brown: #3e2a1f;
    --white: #ffffff;
    --ink: #2b2b2b;
    --soft: #6d6d6d;
    --panel: #f1efec;
    --seal: #c9c4bd;
    --seal-edge: #a9a39b;
  }
  * { margin: 0; padding: 0; box-sizing: border-box; }
  html, body { width: 1200px; height: 785px; overflow: hidden; }
  body {
    background: var(--bg);
    font-family: "Arimo", Arial, sans-serif;
    position: relative;
  }
  .card {
    position: absolute;
    top: 242px;
    width: 520px;
    height: 300px;
    box-shadow: 0 6px 18px rgba(0,0,0,.18);
  }

  /* Front side */
  .card--front { left: 60px; background: var(--brown); color: var(--white); }
  .front-brand {
    position: absolute; inset: 0;
    display: flex; align-items: center; justify-content: center; gap: 16px;
  }
  .brand-square { width: 26px; height: 26px; background: currentColor; flex: none; }
  .front-name { font-weight: 700; font-size: 40px; line-height: 1; }

  /* Back side */
  .card--back { left: 620px; background: var(--white); color: var(--ink); }
  .back-panel {
    position: absolute; left: 0; top: 0; width: 215px; height: 100%;
    background: var(--panel);
  }
  .back-brand {
    position: absolute; left: 24px; top: 96px; width: 170px;
    display: flex; align-items: center; gap: 10px; color: var(--brown);
  }
  .back-brand .brand-square { width: 16px; height: 16px; }
  .back-name { font-weight: 700; font-size: 22px; line-height: 1; white-space: nowrap; }
  .credential {
    position: absolute; left: 24px; top: 180px; width: 180px;
    display: flex; align-items: center; gap: 10px; color: var(--brown);
  }
  .credential-seal {
    width: 40px; height: 40px; border-radius: 50%; flex: none;
    background: var(--seal); border: 2px solid var(--seal-edge);
  }
  .credential-text { font-size: 13px; line-height: 1.25; }
  .contact {
    position: absolute; left: 240px; top: 44px;
    font-size: 15px; line-height: 1.3;
  }
  .contact-name { font-weight: 700; font-size: 17px; }
  .contact-role { color: var(--soft); margin-bottom: 18px; }
  .contact-address { margin-bottom: 16px; }
</style>
</head>
<body>
  <section class="card card--front" aria-label="Business card front">
    <div class="front-brand">
      <span class="brand-square"></span>
      <span class="front-name">Keelvale Group</span>
    </div>
  </section>

  <section class="card card--back" aria-label="Business card back">
    <div class="back-panel"></div>
    <div class="back-brand">
      <span class="brand-square"></span>
      <span class="back-name">Keelvale Group</span>
    </div>
    <div class="credential">
      <span class="credential-seal" role="img" aria-label="Accreditation badge"></span>
      <div class="credential-text">Certified<br>Works Overseer</div>
    </div>
    <div class="contact">
      <div class="contact-name">Alan Reyes</div>
      <div class="contact-role">Managing Director</div>
      <div class="contact-address">48 Harlow Lane<br>Eastvale 3100, Victoria</div>
      <div>Telephone: 03 0000 0000</div>
      <div>Fax: 03 0000 0000</div>
      <div>Mobile: 03 0000 0000</div>
    </div>
  </section>
</body>
</html>
```